Jahresprogramm für kirchliche Organisation
Zielgruppe
Wir sind die Berufungspastoralstelle im Bistum Halbrode der katholischen Kirche. Wir kümmen uns um die Frage nach der Berufung von jungen Menschen zwischen 17-30 Jahren. Unter Berufung verstehen wir die Frage nach dem Plan Gottes für das eigene Leben
Aufgabenstellung
Es geht um eine Designvorlage für eine Jahresprospekt unserer Stelle, die wir leicht wieder ändern oder ergänzen können (Grafikprogrammgrundkenntnisse sind vorhanden), da manche Termine noch nicht letzlich feststehen.
Vom Design darf es sich gerne an unserer Homepage https://www.lebenswegstelle-halbrode.de/ orientieren.
Wenn möglich gerne im Endformat DIN lang quer (210 x 105 mm)

```html
<!DOCTYPE html>
<html lang="de">
<head>
<meta charset="utf-8">
<title>Jahresprogramm 2022 – Bistum Halbrode</title>
<link rel="stylesheet" href="https://fonts.googleapis.com/css2?family=Open+Sans:wdth,wght@75,300;75,400;75,700&display=swap">
<style>
  :root {
    --page: #ffffff;
    --gold: #e2b428;
    --gold-light: #ebc445;
    --ink: #ffffff;
    --dark: #2b2b2b;
    --black: #000000;
    --photo-light: #e9ddd8;
    --photo-mid: #c6b0a4;
    --photo-dark: #9c8676;
  }
  * { margin: 0; padding: 0; box-sizing: border-box; }
  html, body {
    width: 1200px; height: 675px; overflow: hidden;
    background: var(--page);
    font-family: "Open Sans", Arial, sans-serif;
    font-stretch: 75%;
  }
  .flyer {
    position: absolute; left: 153px; top: 114px;
    width: 893px; height: 449px;
    display: flex;
    box-shadow: 0 2px 8px rgba(0,0,0,0.28);
  }
  .cover-photo {
    width: 380px; height: 100%;
    background:
      radial-gradient(ellipse 30% 55% at 48% 40%, #f4f1ee 0%, rgba(244,241,238,0) 100%),
      linear-gradient(180deg, var(--photo-light) 0%, var(--photo-mid) 55%, var(--photo-dark) 100%);
  }
  .title-panel {
    width: 276px; height: 100%;
    background: radial-gradient(circle at 40% 30%, var(--gold-light), var(--gold) 70%);
    color: var(--ink);
    text-align: right;
    padding-right: 50px;
  }
  .year {
    font-weight: 700; font-size: 64px; line-height: 1;
    margin-top: 168px;
  }
  .motto {
    font-weight: 300; font-size: 28px; line-height: 1.3;
    margin-top: 40px;
  }
  .brand-panel {
    position: relative;
    width: 237px; height: 100%;
    background: var(--page);
  }
  .diocese {
    position: absolute; left: 32px; top: 88px;
    display: flex; align-items: center; gap: 8px;
    font-size: 18px; font-weight: 400; letter-spacing: 0.06em;
    text-transform: uppercase; color: var(--dark);
  }
  .diocese-mark { width: 16px; height: 16px; background: #5c8fc7; }
  .program-name {
    position: absolute; left: 28px; top: 178px;
    display: flex; align-items: center; gap: 10px;
    font-size: 30px; font-weight: 400; color: var(--dark);
  }
  .program-mark {
    width: 40px; height: 40px; border-radius: 50%;
    border: 3px solid var(--gold);
  }
  .brand-bar {
    position: absolute; left: 0; bottom: 0;
    width: 100%; height: 35px; background: var(--black);
  }
</style>
</head>
<body>
  <div class="flyer">
    <div class="cover-photo" role="img" aria-label="Foto: barfüßige Person in weißem Gewand geht auf einem sandigen Weg"></div>
    <div class="title-panel">
      <p class="year">2022</p>
      <p class="motto">Komm und sieh!<br>Joh 1,46</p>
    </div>
    <div class="brand-panel">
      <div class="diocese"><span class="diocese-mark"></span>Bistum Halbrode</div>
      <div class="program-name"><span class="program-mark"></span>Weg &amp; Ziel</div>
      <div class="brand-bar"></div>
    </div>
  </div>
</body>
</html>
```